Independent IT Consulting Professional. Looking for a clean crisp, somewhat traditional design. I have also attached the initial off-the-shelf design from PrintHaven. My company has grown quickly, and I would like to take the card to the next level. Should be sharp, mature, classy well laid-out and convey confidence. I don't think the off-the-shelf design does this. I like the logo I have for the time being, but if someone has something better in mind, I would be happy to consider an alternative. I would also like to see the color Cyan used in a small way, either with the logo or some other color treatment, as I feel like this is a modern color that I always liked, but never was able to make anything work with it.
Industry/Entity Type
It Company
Contact Information for Business Card
Carter J. Whitlow
Owner
TrellMark Solutions
2817 Ashborough Lane
Pinehollow, NY 13000
(917) 555-0148
cwhitlow@trellmarksolutions.example
www.trellmarksolutions.example
Tagline: Business Technology Services and Consulting

```html
<!DOCTYPE html>
<html lang="en">
<head>
<meta charset="utf-8">
<title>TrellMark Solutions – Business Card</title>
<link rel="stylesheet" href="https://fonts.googleapis.com/css2?family=Arimo:wght@400;700&display=swap">
<style>
  :root {
    --stage: #000000;
    --card: #ffffff;
    --ink: #111111;
    --teal: #149b9a;
    --cyan: #2bb3b1;
    --on-teal: #ffffff;
  }
  * { box-sizing: border-box; margin: 0; padding: 0; }
  html, body { width: 1200px; height: 900px; overflow: hidden; background: var(--stage); }
  body { font-family: "Arimo", Arial, sans-serif; color: var(--ink); }

  .canvas { position: relative; width: 1200px; height: 900px; }

  .business-card {
    position: absolute; left: 180px; top: 210px;
    width: 840px; height: 480px;
    background: var(--card); border-radius: 22px; overflow: hidden;
  }

  .brand-mark {
    position: absolute; left: 70px; top: 108px;
    display: flex; align-items: center; gap: 16px;
  }
  .brand-mark__dot { width: 34px; height: 34px; border-radius: 50%; background: var(--cyan); flex: none; }
  .brand-mark__name { font-weight: 700; font-size: 30px; line-height: 1.05; color: var(--ink); }

  .divider {
    position: absolute; left: 345px; top: 73px;
    width: 3px; height: 177px; background: var(--ink);
  }

  .identity { position: absolute; left: 378px; top: 84px; width: 440px; }
  .identity__company { font-weight: 700; font-size: 39px; letter-spacing: -0.2px; }
  .identity__tagline {
    margin: 8px 0 0 46px; width: 300px; text-align: center;
    font-size: 20px; line-height: 1.2;
  }
  .identity__person { margin: 20px 0 0 78px; font-weight: 700; font-size: 27px; }

  .contact-band {
    position: absolute; left: 0; top: 303px; width: 100%; height: 114px;
    background: var(--teal); color: var(--on-teal);
    font-size: 19px; line-height: 1.4;
  }
  .contact-list { position: absolute; list-style: none; }
  .contact-list--postal { left: 60px; top: 16px; }
  .contact-list--online { left: 392px; top: 16px; }
  .contact-item { display: flex; align-items: flex-start; gap: 12px; margin-bottom: 6px; }
  .contact-item svg { width: 16px; height: 16px; margin-top: 5px; flex: none; fill: var(--on-teal); }
</style>
</head>
<body>
<main class="canvas">
  <article class="business-card">
    <div class="brand-mark">
      <span class="brand-mark__dot"></span>
      <span class="brand-mark__name">TrellMark<br>Solutions</span>
    </div>

    <div class="divider"></div>

    <header class="identity">
      <h1 class="identity__company">TrellMark Solutions</h1>
      <p class="identity__tagline">Business Technology Services and Consulting</p>
      <p class="identity__person">Carter J. Whitlow</p>
    </header>

    <section class="contact-band">
      <ul class="contact-list contact-list--postal">
        <li class="contact-item">
          <svg viewBox="0 0 16 16" aria-hidden="true"><path d="M8 0a5.5 5.5 0 0 0-5.5 5.5C2.5 10 8 16 8 16s5.5-6 5.5-10.5A5.5 5.5 0 0 0 8 0zm0 8a2.5 2.5 0 1 1 0-5 2.5 2.5 0 0 1 0 5z"/></svg>
          <span>2817 Ashborough Lane<br>Pinehollow, NY 13000</span>
        </li>
        <li class="contact-item">
          <svg viewBox="0 0 16 16" aria-hidden="true"><path d="M3.6 1l2.3 3.3-1.4 1.7a9 9 0 0 0 5.5 5.5l1.7-1.4L15 12.4 13.3 15C6.5 14.7 1.3 9.5 1 2.7z"/></svg>
          <span>(917) 555-0148</span>
        </li>
      </ul>
      <ul class="contact-list contact-list--online">
        <li class="contact-item">
          <svg viewBox="0 0 16 16" aria-hidden="true"><path d="M1 3h14v10H1z M1 3l7 5 7-5" fill="none" stroke="#fff" stroke-width="1.6"/><path d="M1 3h14L8 8z"/></svg>
          <span>cwhitlow@trellmarksolutions.example</span>
        </li>
        <li class="contact-item">
          <svg viewBox="0 0 16 16" aria-hidden="true"><circle cx="8" cy="8" r="7"/></svg>
          <span>www.trellmarksolutions.example</span>
        </li>
      </ul>
    </section>
  </article>
</main>
</body>
</html>
```